" Trata-se de uma clínica em início de funcionamento. Somos dois responsáveis técnicos (Psicólogos) e temos outros seis profissionais que estarão trabalhando conosco (também psicólogos). Temos uma médica Psiquiatra que fará parte da equipe. Ofereceremos atendimento nas abordagens: terapia cognitivo comportamental, humanista, psicanálise e Gestalt, entretanto, o foco será na Terapia Cognitivo-Comportamental (TCC). De forma breve, a base da TCC é: Nossos pensamentos, emoções e comportamentos estão interligados e influenciam um ao outro e são o foco principal do tratamento. Fazemos atendimentos individuais e em grupo. Além dos atendimentos de psicologia, a nossa proposta é oferecer outros serviços como palestras, cursos, treinamentos. Disponibilizamos de auditório para uso da clínica. No meu caso, tenho forte vínculo acadêmico. Sou pesquisadora do Núcleo de Estudos Clínicos da UNEVAR e faço mestrado em Saúde Mental na mesma instituição. Também pós-graduanda em TCC. Então o ensino será algo que terá um investimento forte, juntamente com os atendimentos clínicos. "

```html
<!DOCTYPE html>
<html lang="pt-BR">
<head>
<meta charset="UTF-8">
<title>Mentis Psicologia – Capa da página</title>
<link rel="stylesheet" href="https://fonts.googleapis.com/css2?family=Advent+Pro:wght@300&family=Roboto:wght@400;700&display=swap">
<style>
  :root {
    --backdrop: #eceef1;
    --page-bg: #e9ebee;
    --panel: #ffffff;
    --navy: #0d2b47;
    --navy-soft: #1d4466;
    --teal: #4d9f98;
    --teal-light: #6cc0b3;
    --white: #ffffff;
    --fb-text: #1d2129;
    --fb-muted: #90949c;
    --fb-border: #dddfe2;
    --fb-blue: #4267b2;
    --btn-bg: #f6f7f9;
  }
  * { box-sizing: border-box; margin: 0; padding: 0; }
  html, body { width: 1200px; height: 1200px; overflow: hidden; }
  body { background: var(--backdrop); position: relative; font-family: 'Roboto', Arial, sans-serif; }

  .page {
    position: absolute; left: 19px; top: 384px; width: 1162px; height: 432px;
    background: var(--page-bg); box-shadow: 0 2px 8px rgba(0,0,0,.12);
  }
  .sidebar { position: absolute; left: 0; top: 0; width: 221px; height: 100%; }
  .profile-picture {
    position: absolute; left: 15px; top: 19px; width: 187px; height: 187px;
    background: var(--navy); border: 5px solid var(--white);
    display: flex; align-items: center; justify-content: center; gap: 8px;
  }
  .brand-mark { display: inline-block; border-radius: 50%; background: var(--teal-light); flex: none; }
  .brand-name {
    font-family: 'Advent Pro', sans-serif; font-weight: 300; color: var(--white);
    line-height: 1; white-space: nowrap;
  }
  .profile-picture .brand-mark { width: 18px; height: 18px; }
  .profile-picture .brand-name { font-size: 24px; }

  .page-name { position: absolute; left: 19px; top: 232px; font-size: 20px; font-weight: 700; color: var(--fb-text); }
  .page-handle { position: absolute; left: 19px; top: 264px; font-size: 15px; color: var(--fb-muted); }
  .page-nav { position: absolute; left: 0; top: 300px; width: 213px; list-style: none; }
  .page-nav li { height: 40px; line-height: 40px; padding-left: 19px; font-size: 16px; color: var(--fb-text); }
  .page-nav li.active { background: var(--panel); font-weight: 700; border-left: 3px solid var(--fb-blue); padding-left: 16px; }

  .cover {
    position: absolute; left: 221px; top: 0; width: 941px; height: 365px;
    background: var(--navy); overflow: hidden;
  }
  .cover svg { position: absolute; left: 0; top: 0; }
  .cover-pattern {
    position: absolute; right: 0; top: 0; width: 470px; height: 300px;
    background: radial-gradient(ellipse at 70% 45%, var(--navy-soft) 0%, rgba(29,68,102,.55) 45%, rgba(13,43,71,0) 75%);
  }
  .cover-logo {
    position: absolute; left: 0; top: 120px; width: 941px;
    display: flex; align-items: center; justify-content: center; gap: 22px;
  }
  .cover-logo .brand-mark { width: 56px; height: 56px; }
  .cover-logo .brand-name { font-size: 72px; }

  .action-bar {
    position: absolute; left: 221px; top: 370px; width: 941px; height: 48px;
    background: var(--panel); border: 1px solid var(--fb-border);
    display: flex; align-items: center; padding: 0 12px; gap: 8px;
  }
  .action-btn {
    height: 32px; padding: 0 14px; border: 1px solid var(--fb-border); border-radius: 3px;
    background: var(--btn-bg); font-size: 14px; font-weight: 700; color: #4b4f56;
    display: flex; align-items: center;
  }
  .send-message {
    margin-left: auto; width: 342px; height: 32px; border-radius: 3px;
    background: var(--fb-blue); color: var(--white); font-size: 15px; font-weight: 700;
    display: flex; align-items: center; justify-content: center;
  }
</style>
</head>
<body>
  <main class="page">
    <aside class="sidebar">
      <div class="profile-picture">
        <span class="brand-mark"></span>
        <span class="brand-name">Mentis Psicologia</span>
      </div>
      <h1 class="page-name">Mentis Psicologia</h1>
      <p class="page-handle">@Mentis Psicologia</p>
      <ul class="page-nav">
        <li class="active">Home</li>
        <li>Posts</li>
        <li>Videos</li>
      </ul>
    </aside>

    <section class="cover">
      <div class="cover-pattern" role="img" aria-label="Padrão decorativo de círculos sobrepostos em tons de azul"></div>
      <svg width="941" height="365" viewBox="0 0 941 365" aria-hidden="true">
        <path d="M0 300 Q 430 200 941 255 L941 365 L0 365 Z" fill="var(--teal-light)"/>
        <path d="M0 312 Q 430 214 941 268 L941 365 L0 365 Z" fill="var(--teal)"/>
      </svg>
      <div class="cover-logo">
        <span class="brand-mark"></span>
        <span class="brand-name">Mentis Psicologia</span>
      </div>
    </section>

    <nav class="action-bar">
      <span class="action-btn">Liked ▾</span>
      <span class="action-btn">Following ▾</span>
      <span class="action-btn">Share</span>
      <span class="action-btn">···</span>
      <span class="send-message">Send Message</span>
    </nav>
  </main>
</body>
</html>
```